Every Drawer Neatly Sorted or EDN Organized needs a business card design. EDN Organized is a professi

We need a business card design that is clean, sharp and conveys a sense of organization. I already have a logo.

Target Market(s)

Families (specifically mothers), small business owners, parents, seniors

Industry/Entity Type

Business

Contact Information for Business Card

My website is www.ednorganized-example.com and my Facebook page is http://www.socialpage-example.com/everydrawerneatlysorted. The phone number is 555-418-2706 and I want to be listed as Miriel O. Dunsford, Owner

Requirements
Must have
• My logo.

```html
<!DOCTYPE html>
<html lang="en">
<head>
<meta charset="utf-8">
<title>EDN Organized — Business Card</title>
<link rel="stylesheet" href="https://fonts.googleapis.com/css2?family=Raleway:wght@300;400&family=Arimo:wght@400&display=swap">
<style>
  :root {
    --backdrop: #d9d4cc;
    --card-black: #050607;
    --card-sheen: #24272b;
    --accent-blue: #3f8fd0;
    --text-white: #f2f4f6;
  }
  * { margin: 0; padding: 0; box-sizing: border-box; }
  html, body {
    width: 1200px;
    height: 1022px;
    overflow: hidden;
    background: var(--backdrop);
  }
  .card {
    position: absolute;
    left: 100px;
    top: 226px;
    width: 1000px;
    height: 570px;
    border-radius: 26px;
    overflow: hidden;
    background:
      radial-gradient(ellipse 70% 80% at 35% 45%, var(--card-sheen) 0%, rgba(20,22,25,0.6) 45%, transparent 80%),
      var(--card-black);
    box-shadow: 0 18px 40px rgba(0,0,0,0.35);
  }
  .divider {
    position: absolute;
    left: 0;
    top: 360px;
    width: 100%;
    height: 2px;
    background: var(--accent-blue);
  }
  .brand-mark {
    position: absolute;
    left: 56px;
    top: 252px;
    display: flex;
    align-items: center;
    gap: 12px;
  }
  .brand-dot {
    width: 26px;
    height: 26px;
    border-radius: 50%;
    background: var(--accent-blue);
  }
  .brand-name {
    font-family: 'Raleway', sans-serif;
    font-weight: 400;
    font-size: 32px;
    line-height: 1;
    color: var(--accent-blue);
    white-space: nowrap;
  }
  .tagline-small {
    position: absolute;
    left: 384px;
    top: 150px;
    font-family: 'Raleway', sans-serif;
    font-weight: 300;
    font-size: 36px;
    letter-spacing: 5px;
    color: var(--text-white);
    white-space: nowrap;
  }
  .tagline-large {
    position: absolute;
    left: 378px;
    top: 196px;
    font-family: 'Raleway', sans-serif;
    font-weight: 300;
    font-size: 88px;
    line-height: 1;
    letter-spacing: 22px;
    color: var(--text-white);
    white-space: nowrap;
  }
  .person-name {
    position: absolute;
    left: 505px;
    top: 304px;
    font-family: 'Arimo', sans-serif;
    font-size: 40px;
    line-height: 1;
    color: var(--accent-blue);
    white-space: nowrap;
  }
  .person-role {
    position: absolute;
    left: 745px;
    top: 374px;
    font-family: 'Arimo', sans-serif;
    font-size: 22px;
    color: var(--text-white);
  }
  .contact-list {
    position: absolute;
    left: 384px;
    top: 418px;
    list-style: none;
    font-family: 'Arimo', sans-serif;
    font-size: 21px;
    line-height: 34px;
    color: var(--text-white);
    white-space: nowrap;
  }
  .contact-label { color: var(--accent-blue); margin-right: 6px; }
</style>
</head>
<body>
  <section class="card" aria-label="EDN Organized business card">
    <div class="divider"></div>
    <div class="brand-mark">
      <span class="brand-dot" aria-hidden="true"></span>
      <span class="brand-name">EDN Organized</span>
    </div>
    <div class="tagline-small">Every Drawer Neatly</div>
    <div class="tagline-large">SORTED</div>
    <div class="person-name">Miriel O. Dunsford</div>
    <div class="person-role">Owner</div>
    <ul class="contact-list">
      <li><span class="contact-label">P:</span>555-418-2706</li>
      <li><span class="contact-label">W:</span>www.ednorganized-example.com</li>
      <li><span class="contact-label">F:</span>www.socialpage-example.com/everydrawerneatlysorted</li>
    </ul>
  </section>
</body>
</html>
```